**Promotional Flyer for Charity Golf Event**

Create a promotional flyer for a Charity Golf Event

Target Market(s)

Golfers wanting to play in a charity/corporate golf event

Industry/Entity Type

Non Profit

Requirements
Must have
• The flyer must have the logo of the charity (Bluefinch), must have the logo of the Golf Event (Tarn Invitational) and the Morvale Logo and the text supplied.
• Photo supplied to also be included

```html
<!DOCTYPE html>
<html lang="en">
<head>
<meta charset="utf-8">
<title>Tarn Invitational – Charity Golf Day</title>
<link href="https://fonts.googleapis.com/css2?family=Arimo:wght@400;700&display=swap" rel="stylesheet">
<style>
  :root {
    --backdrop: #c9ccc8;
    --paper: #ffffff;
    --green: #1a7f12;
    --ink: #111111;
    --grey: #8c9a9a;
    --turf-light: #7fc646;
    --turf-dark: #2f6e1a;
  }
  html, body { margin: 0; padding: 0; width: 1200px; height: 1200px; overflow: hidden; background: var(--backdrop); font-family: "Arimo", Arial, sans-serif; }
  .flyer { position: absolute; left: 200px; top: 65px; width: 800px; height: 1070px; background: var(--paper); overflow: hidden; }
  .block { position: absolute; color: var(--ink); font-size: 14.4px; line-height: 17.6px; }
  .block h2 { margin: 0; font-weight: 400; font-size: 14.4px; color: var(--green); }
  .block ul { list-style: none; margin: 0; padding: 0; }
  .block li::before { content: "• "; }
  .block p { margin: 0; }
  .play { left: 64px; top: 98px; }
  .prizes { left: 64px; top: 152px; }
  .divider { position: absolute; left: 302px; top: 74px; width: 4px; height: 279px; background: var(--green); }
  .schedule { left: 346px; top: 87px; }
  .tickets { left: 346px; top: 196px; width: 400px; }
  .tickets .price { margin-top: 18px; }
  .tickets ul { margin-top: 18px; }
  .support { left: 114px; top: 405px; width: 580px; font-size: 11.2px; line-height: 14.4px; z-index: 2; }
  .support h2 { font-size: 11.2px; margin-top: 14px; }
  .support .gap { margin-top: 14px; }
  .turf { position: absolute; left: 0; top: 0; width: 800px; height: 1070px; }
  .brand { position: absolute; left: 392px; top: 930px; display: flex; align-items: center; gap: 10px; color: var(--green); font-size: 22px; font-weight: 700; }
  .brand .mark { width: 34px; height: 34px; background: #e2561a; }
  .event { position: absolute; left: 540px; top: 920px; color: var(--green); font-weight: 700; font-size: 30px; line-height: 34px; width: 200px; }
  .date { position: absolute; left: 542px; top: 1000px; color: var(--grey); font-weight: 700; font-size: 17px; letter-spacing: 6px; }
</style>
</head>
<body>
<div class="flyer">
  <svg class="turf" viewBox="0 0 800 1070" role="img" aria-label="Photo of a gloved hand teeing up a golf ball beside a driver on a green fairway with a flag in the distance">
    <defs>
      <linearGradient id="turfFade" x1="0" y1="0" x2="0" y2="1">
        <stop offset="0" stop-color="#ffffff"/>
        <stop offset="0.22" stop-color="#ffffff"/>
        <stop offset="0.42" stop-color="var(--turf-dark)"/>
        <stop offset="0.7" stop-color="var(--turf-light)"/>
        <stop offset="1" stop-color="var(--turf-dark)"/>
      </linearGradient>
    </defs>
    <polygon points="0,440 800,440 800,820 0,992" fill="url(#turfFade)"/>
  </svg>

  <div class="block play">
    <h2>Play format</h2>
    <ul><li>4 ball ambrose, shotgun start</li></ul>
  </div>
  <div class="block prizes">
    <h2>Great Event Prizes</h2>
    <ul>
      <li>Perpetual Tarn Invitational Trophy</li>
      <li>Longest Drive Trophy</li>
      <li>Nearest to the Pin</li>
    </ul>
  </div>

  <div class="divider"></div>

  <div class="block schedule">
    <h2>Format</h2>
    <ul>
      <li>1 pm Registration and light lunch at Harlow Ridge Golf Club</li>
      <li>2 pm Shotgun start, play commences</li>
      <li>5 pm Gourmet BBQ and drinks – presentation and prizes</li>
      <li>7.30 pm Finish</li>
    </ul>
  </div>
  <div class="block tickets">
    <h2>Player and Sponsorship Opportunities</h2>
    <p class="price">Golf-Individual Player $187.50 (tickets can be purchased through Ticketnest.com.au)</p>
    <ul>
      <li>Light lunch</li>
      <li>9 Holes of Golf</li>
      <li>Gourmet BBQ</li>
    </ul>
    <p>Dinner Only - $75</p>
  </div>

  <div class="block support">
    <p>Not a golfer but keen to support the Inaugural MORVALE TARN Invitational and Bluefinch, then why not join us and be inspired</p>
    <h2>Sponsorship Opportunities:</h2>
    <p>We have opportunities for Hole Sponsors, as well as a Drink Cart Sponsor that start from $1,300 please email jana.ward@morvalegroup.com</p>
    <p class="gap">Come along and join us in supporting Bluefinch as they provide essential services<br>to children young people and their families with cancer.</p>
  </div>

  <div class="brand"><span class="mark"></span>Morvale</div>
  <div class="event">Tarn Invitational</div>
  <div class="date">09.22.2017</div>
</div>
</body>
</html>
```